Private law enforcement protective services needs a kick ass brochure

We need a brochure that tops the security competition. We are a Pennsylvania based company providing law enforcement officers to the private sector to take the place of regular security officers. We are peacekeepers with the powers of arrest for any major crime committed in our presence. Our customers will get so much more by using our services over regular security. All of our officers attend annual training to stay up to date and sharp in their skills. We would like to see a design that uses the colors Royal blue, black, and grays. The final design should communicate better service over regular security yet have that soft touch and caring feeling. We want to be taken serious yet not scary. We want prospective customers to say WOW... we need to use them rather than regular security guards. We also offer K-9 services. Drug searches as well as explosive searches. THIS NEEDS TO GO ON A TRI FOLD BROCHURE. I already have a website. Www.marlowridgepatrol.com

Target Market(s)

Any business or entity where security or protective services will be needed. We provide services for events like Fairs, carnivals, churches, retail stores, large events, hostile terminations, post disaster sites, overarching of work crews in hostile areas, special celebrations, parades, sporting events,

Industry/Entity Type

Security Service

Font styles to use
Sans Serif

Requirements
Must have
• We need to have a strong professional look yet not too aggressive. DO NOT CALL OUR SERVICES SECURITY !!!! We are PEACEKEEPERS. We Keep the Peace. We provide services all across the state of Pennsylvania. We are one of Pennsylvania's best kept secrets.
Nice to have
• Pictures of Police cars, Officers on patrol at an event,

```html
<!DOCTYPE html>
<html lang="en">
<head>
<meta charset="utf-8">
<title>Marlow Ridge Patrol – Tri-fold Brochure</title>
<link href="https://fonts.googleapis.com/css2?family=Montserrat:ital,wght@0,300;0,500;0,700;0,800;1,600&family=PT+Serif&display=swap" rel="stylesheet">
<style>
:root{
  --royal:#3a44a6;
  --royal-dark:#2c3486;
  --ink:#141414;
  --paper:#f4f4f5;
  --gray:#d9d9dc;
  --gray-mid:#a9a9ae;
  --white:#ffffff;
  --stage:#3c3c3e;
}
*{margin:0;padding:0;box-sizing:border-box}
html,body{width:768px;height:1200px;overflow:hidden;background:var(--stage)}
.canvas{position:relative;width:768px;height:1200px}
.spread{position:absolute;left:12px;width:744px;height:578px;display:flex;box-shadow:0 8px 24px rgba(0,0,0,.45)}
.spread--outside{top:8px}
.spread--inside{top:614px}
.panel{position:relative;width:248px;height:100%;overflow:hidden;background:linear-gradient(160deg,var(--white),var(--paper) 55%,var(--gray))}
.panel + .panel{border-left:1px solid rgba(0,0,0,.08)}
.serif{font-family:"PT Serif",serif}
.sans{font-family:"Montserrat",sans-serif}
.photo{position:absolute}

/* testimonials */
.testimonials__title{position:absolute;left:18px;top:36px;font:800 22px "Montserrat",sans-serif;letter-spacing:2px;color:var(--royal)}
.testimonials__rule{position:absolute;left:18px;top:66px;width:210px;height:1px;background:var(--ink)}
.quote{position:absolute;left:18px;width:212px;font:7.4px/1.45 "PT Serif",serif;color:var(--ink)}
.quote__mark{font:800 30px/1 "Montserrat",sans-serif;color:var(--ink);display:block;height:20px}
.quote__mark--close{text-align:right;margin-top:-4px}
.quote__name{text-align:right;font:600 8.5px "Montserrat",sans-serif;color:var(--royal)}
.quote__role{text-align:right;font:700 8px "Montserrat",sans-serif;color:var(--royal)}
.wedge{position:absolute;background:var(--royal)}

/* contact panel */
.mission{position:absolute;left:18px;right:18px;top:48px;text-align:center;font:11px/1.4 "PT Serif",serif;color:var(--ink)}
.contact-box{position:absolute;left:32px;right:32px;top:176px;border:1.5px solid var(--royal);border-radius:8px;padding:8px 0 6px;text-align:center;background:var(--white)}
.contact-box__top{font:700 19px "Montserrat",sans-serif;color:var(--ink);letter-spacing:1px}
.contact-box__bottom{font:800 19px "Montserrat",sans-serif;color:var(--royal);letter-spacing:1px}
.contact-band{position:absolute;left:0;right:0;bottom:0;height:130px;background:var(--ink);clip-path:polygon(0 14%,100% 0,100% 100%,0 100%);color:var(--white);text-align:center;padding-top:34px}
.contact-band__phone{font:700 21px "Montserrat",sans-serif;display:flex;align-items:center;justify-content:center;gap:6px}
.contact-band__web{font:500 9px "Montserrat",sans-serif;margin-top:8px}

/* cover */
.wordmark{position:absolute;left:20px;right:20px;top:90px;display:flex;align-items:center;gap:10px}
.wordmark__dot{width:34px;height:34px;border-radius:50%;background:var(--royal);flex:none}
.wordmark__name{font:800 24px/1.05 "Montserrat",sans-serif;color:var(--royal)}
.cover__icon-row{position:absolute;left:20px;right:20px;top:250px;display:flex;align-items:center;gap:8px}
.cover__icon-row .line{flex:1;height:1px;background:var(--royal)}
.icon-circle{width:24px;height:24px;border-radius:50%;background:var(--royal);display:flex;align-items:center;justify-content:center}
.cover__phone{position:absolute;left:0;right:0;top:284px;text-align:center;font:800 25px "Montserrat",sans-serif;color:var(--royal-dark)}
.cover__webbar{position:absolute;left:14px;right:14px;top:322px;background:var(--ink);color:var(--white);text-align:center;font:500 9.5px/20px "Montserrat",sans-serif}
.cover__band{position:absolute;left:0;right:0;bottom:0;height:215px;background:var(--royal);clip-path:polygon(0 18%,100% 0,100% 100%,0 100%);text-align:center;padding-top:78px}
.cover__state{font:800 22px "Montserrat",sans-serif;color:var(--white);letter-spacing:1px}
.cover__tag{display:inline-block;margin-top:6px;background:var(--white);color:var(--royal);font:800 19px "Montserrat",sans-serif;padding:3px 12px}

/* inside */
.panel--dark{background:linear-gradient(180deg,#1b1b1c,#262523 60%,#3a2d1e)}
.section-head{font:300 22px "Montserrat",sans-serif;letter-spacing:1px}
.section-head b{font-weight:800}
.who__head{position:absolute;left:18px;top:34px;color:var(--white)}
.who__rule{position:absolute;left:18px;top:64px;width:210px;height:1px;background:var(--white)}
.who__body{position:absolute;left:18px;right:16px;top:74px;color:#eee;font:7.3px/1.42 "PT Serif",serif}
.who__body p{margin-bottom:6px}
.services__head{position:absolute;left:16px;top:34px;color:var(--ink)}
.services__head b{color:var(--royal)}
.ribbon{position:absolute;background:var(--royal);color:var(--white);font:700 11px/22px "Montserrat",sans-serif;letter-spacing:.5px;padding:0 22px 0 12px;clip-path:polygon(0 0,calc(100% - 14px) 0,100% 100%,0 100%)}
.ribbon::after{content:""}
.body-copy{position:absolute;font:7.3px/1.42 "PT Serif",serif;color:var(--ink)}
.ticks{position:absolute;list-style:none;font:500 10px/1.55 "Montserrat",sans-serif;color:var(--ink)}
.ticks li{display:flex;align-items:center;gap:6px}
.ticks li::before{content:"✓";flex:none;width:10px;height:10px;border:1px solid var(--royal);border-radius:50%;font:700 6px/9px "Montserrat",sans-serif;color:var(--royal);text-align:center}
.ticks--small{font-size:9.2px}
</style>
</head>
<body>
<main class="canvas">

  <section class="spread spread--outside" aria-label="Outside of brochure">
    <article class="panel panel--testimonials">
      <h2 class="testimonials__title">TESTIMONIALS</h2>
      <div class="testimonials__rule"></div>
      <blockquote class="quote" style="top:74px">
        <span class="quote__mark">“</span>
        Our law firm regularly uses the services of Marlow Ridge Patrol to serve subpoenas and other legal notices. Their team does a great job at a reasonable price. Sometimes the recipients try and duck service, but their officers work diligently to ensure they are served in a timely and professional manner. We recommend them.
        <span class="quote__mark quote__mark--close">”</span>
        <div class="quote__name">Dana Whitcombe</div>
        <div class="quote__role">Whitcombe Hale Law, P.C.</div>
      </blockquote>
      <blockquote class="quote" style="top:206px">
        <span class="quote__mark">“</span>
        I am a safety lead who worked on a pipeline project in Pennsylvania. After an unfortunate incident, we hired Officer Tom Hensley and his team to maintain the peace for the safety and protection of our employees and equipment. He organized a team and was working the next day. All were very professional, friendly and very knowledgeable of what needed to be done. As their point of contact, they were all communicative. Thanks to those guys we were able to finish the job safely and I made some great friends as well.
        <span class="quote__mark quote__mark--close">”</span>
        <div class="quote__name">Reed Calloway</div>
        <div class="quote__role">Safety Lead</div>
      </blockquote>
      <div class="photo" role="img" aria-label="Photo of a sidearm and a state constable patch on a dark table" style="left:0;right:0;top:382px;bottom:0;background:linear-gradient(150deg,#6c665c,#2e2b27 55%,#151412);clip-path:polygon(0 22%,100% 0,100% 100%,0 100%)"></div>
      <div class="wedge" style="right:0;bottom:0;width:170px;height:50px;clip-path:polygon(100% 0,100% 100%,0 100%)"></div>
    </article>

    <article class="panel panel--contact">
      <p class="mission">A proven leader in providing professionally trained and certified Constables throughout the Commonwealth of Pennsylvania. Let our Pennsylvania State Constables give you the peace of mind you deserve.</p>
      <div class="contact-box">
        <div class="contact-box__top">CONTACT US</div>
        <div class="contact-box__bottom">TODAY!</div>
      </div>
      <div class="photo" role="img" aria-label="Photo of a patrol car at night with red and blue lights" style="left:0;right:0;top:250px;height:230px;background:radial-gradient(circle at 40% 35%,#c2253a 0,transparent 22%),radial-gradient(circle at 70% 40%,#3b4fc0 0,transparent 28%),linear-gradient(180deg,#3a2c3a,#1c1c2a 60%,#2a2f52)"></div>
      <div class="wedge" style="left:0;bottom:0;width:248px;height:80px;clip-path:polygon(0 100%,100% 30%,100% 100%)"></div>
      <div class="contact-band">
        <div class="contact-band__phone">
          <svg width="18" height="18" viewBox="0 0 24 24" aria-hidden="true"><circle cx="12" cy="12" r="10.5" fill="none" stroke="#fff" stroke-width="2"/><path d="M8.5 6.5l2 2.5-1.2 1.5c.8 1.7 2 2.9 3.7 3.7l1.5-1.2 2.5 2-1.3 2c-4.5-.3-8-3.8-8.3-8.3z" fill="#fff"/></svg>
          (717) 555-0142
        </div>
        <div class="contact-band__web">Www.marlowridgepatrol.com</div>
      </div>
    </article>

    <article class="panel panel--cover">
      <div class="wordmark">
        <span class="wordmark__dot"></span>
        <span class="wordmark__name">MARLOW RIDGE PATROL</span>
      </div>
      <div class="cover__icon-row">
        <span class="line"></span>
        <span class="icon-circle"><svg width="12" height="12" viewBox="0 0 24 24" aria-hidden="true"><path d="M5 3l4 5-2.4 3c1.6 3.3 3.9 5.6 7.3 7.3l3-2.4 5 4-2.6 4C10.5 23.3 3.7 16.5 3 7.4z" fill="#fff"/></svg></span>
        <span class="line"></span>
      </div>
      <div class="cover__phone">(717) 555-0142</div>
      <div class="cover__webbar">Www.marlowridgepatrol.com</div>
      <div class="cover__band">
        <div class="cover__state">PENNSYLVANIA</div>
        <div class="cover__tag">STATE CONSTABLE</div>
      </div>
    </article>
  </section>

  <section class="spread spread--inside" aria-label="Inside of brochure">
    <article class="panel panel--dark">
      <h2 class="section-head who__head">WHO <b>WE ARE</b></h2>
      <div class="who__rule"></div>
      <div class="who__body">
        <p>Under Pennsylvania Law, Constables are Public Officers elected or appointed to their position in accordance with the laws of elections.</p>
        <p>A Constable is a sworn Law Enforcement/Peace Officer that can arrest for felony crimes and breaches of peace committed in his presence, or by warrant anywhere in the Commonwealth.</p>
        <p>A Constable is also an officer empowered to carry out the business of the statewide district court system by serving warrants of arrest, mental health warrants, transporting prisoners, service of summons, complaints and subpoenas, and enforcing protection from abuse orders, as well as orders of eviction and judgement levies.</p>
        <p>Constables are also charged with maintaining order at the election polls and ensuring that no qualified elector is obstructed from voting. Constables are the only law enforcement officials permitted at the polls on election day.</p>
        <p>While Constables primarily serve the Courts, they belong to the executive branch of government.</p>
        <p>Constables are elected at the municipal level, however, State law governs Constables. They have statewide authority, thus, the title became “State Constable.”</p>
        <p>Constables are empowered to enforce both criminal and civil laws. Police officers are empowered to enforce criminal and traffic laws. The sheriff is empowered to enforce criminal, civil, and traffic laws. The District Attorney is the chief law enforcement officer of the County.</p>
      </div>
      <div class="photo" role="img" aria-label="Photo of a constable badge and handcuffs on a dark surface" style="left:0;right:0;top:432px;bottom:0;background:radial-gradient(ellipse at 45% 55%,#8a6a3a 0,#3a2a18 45%,transparent 75%)"></div>
    </article>

    <article class="panel panel--services">
      <h2 class="section-head services__head">OUR <b>SERVICES</b></h2>
      <div class="ribbon" style="left:16px;top:70px">CIVIL PROCESS</div>
      <p class="body-copy" style="left:16px;right:14px;top:100px">Pennsylvania State Constables are widely utilized to perform various forms of Civil Process. Many private individuals as well as businesses use Constables to serve important private and court-related legal documents. Our Constables will certify your documents were served, as well as give you that added confidence it is handled in a timely manner.</p>
      <ul class="ticks" style="left:16px;top:182px">
        <li>Subpoenas</li>
        <li>Landlord Tenant</li>
        <li>Protection from Abuse ( PFA's )</li>
        <li>Civil Judgements</li>
        <li>Domestic Relations</li>
        <li>Property Recovery</li>
        <li>Civil Documents</li>
      </ul>
      <div class="ribbon" style="left:16px;top:302px">K9 SERVICES</div>
      <p class="body-copy" style="left:16px;right:14px;top:332px">We are excited to announce that we now offer K9 services. Our K9s are certified and cross-trained in Narcotics, Explosives, Tracking and Apprehension. Our K9 handlers are trained and experienced. You won't find a more professional K9 service around. Contact us today to find out more about our K9 Services offered.</p>
      <div class="photo" role="img" aria-label="Photo of a handler with a search dog checking a bag" style="left:18px;right:18px;top:410px;height:130px;background:linear-gradient(160deg,#cfd2d8,#8c8f98 50%,#5a5650)"></div>
    </article>

    <article class="panel panel--peace">
      <div class="ribbon" style="left:16px;top:34px">PEACE KEEPING</div>
      <p class="body-copy" style="left:16px;right:14px;top:64px">Our constables are a huge deterrent and can act on an individual committing a crime. If you are holding a large event and need peace of mind that you and your guests are safe, let our constables be the ones to provide it for you.</p>
      <ul class="ticks ticks--small" style="left:16px;top:114px">
        <li>Public Events</li>
        <li>Construction / Utility Job Sites</li>
        <li>Crowd Control</li>
        <li>Retail</li>
        <li>Work Place / Place of Employment</li>
        <li>Emergencies / Disasters</li>
      </ul>
      <div class="photo" role="img" aria-label="Photo of officers on foot patrol at a crowded street event" style="left:18px;right:18px;top:214px;height:190px;background:linear-gradient(170deg,#6f7f95,#4a4c56 40%,#b98a74 85%)"></div>
      <div class="ribbon" style="left:16px;top:424px">TRAFFIC CONTROL</div>
      <p class="body-copy" style="left:16px;right:14px;top:454px">Our Pennsylvania State Constable will maintain peace and order where large crowds have gathered. If you are hosting an event and expect a large crowd or a crowd has gathered for whatever reason, don't leave it to a security guard. Let our trained and experienced constables handle your parking and traffic detail, pedestrian foot traffic, and crowd control.</p>
    </article>
  </section>

</main>
</body>
</html>
```